New Business Card Design for Business Consulting Business

We need a business card design that reflects the simplicity of our business. We partner with our clients to help them deliver change. We are a different kind of business consulting group. We don't just provide you with the theory. We provide you with the leadership and capability to execute change.

Vendora is a professional services organisation that partners with their clients to lead the execution of strategic process and system improvement initiatives. Vendora combines hands on delivery with coaching in best practice methodologies and approaches to build their clients capabilities to ensure their ongoing success in project implementations. Vendora offers business advisory services in Project Management, Business Process Management, Change Management and Business Analytics.

Reason: Hi Designers, Thanks for all of your great designs. There are some really creative and cool ideas. Everyone is really capturing the essence of my business Vendora. I am extending the deadline for the business card design by 6 days as I need to consult my Marketing colleague who won't be back in Australia until Wednesday. I would like to sit down with them and review all of the best designs. The key themes of the things I have really liked on my first review are: 1) Capturing the company website on the back of the card. 2) Including the company logo on the back of the card too. 3) Including the types of services on the back of the card that the company offers - Project Management - Business Process Management - Change Management - Business Analytics 4) Utilising some images on the back of the card Just so everyone knows the colour palette for the Vendora company logo is: R: 0 G: 86 B: 162 or C: 97% M: 73% Y: 4% K: 0% Thanks Gerald

Hi Designers,

Thanks for all of your submissions to date.  I am working through each design and will provide feedback on all the great work.

One thing I would like to ask is if you could submit a version that has my academic credentials under or after my name.  I am not a big fan of doing this but as I am in business consulting it does seem to be quite common.

I hold a Bachelor of Commerce (BCom) and a Master of Business Administration (MBA)

Thanks

Gerald

Hi Designers,

Thanks for all of your fantastic designs.  There are some really great designs here for my business.  I am still in the process of reviewing designs and should have this completed by tomorrow.  Some of the things I have learnt from this round of designs are:

1) I prefer to have the card without my academic qualifications

2) I really like cards that have a blue back

3) I prefer to have my name and title either left or right of centre

I hope this helps and I will endeavour to get through all of the designs tomorrow

Cheers

Gerald

Target Market(s)

We target large corporate organisations

Industry/Entity Type

Leadership

Requirements
Must have
• Must have the following business details

Gerald Huxton - Director
Address: Level 7, 82 Fernhill Road, Melbourne, Australia, 3000
Phone: +61 3 527 481 903
Fax: +61 3 9254 3718
Email: gerald.huxton@vendora-example.com.au
LinkedIn: au.linkedin.com/in/geraldphuxton/
Twiiter: @geraldphuxton
Website: www.vendora-example.com.au

```html
<!DOCTYPE html>
<html lang="en">
<head>
<meta charset="utf-8">
<title>Vendora Business Card</title>
<link rel="stylesheet" href="https://fonts.googleapis.com/css2?family=Quicksand:wght@500;600;700&display=swap">
<style>
  :root {
    --backdrop: #3a3634;
    --card: #f2f1ee;
    --brand-blue: #0056a2;
    --text-blue: #1a6aa6;
  }
  * { box-sizing: border-box; margin: 0; padding: 0; }
  html, body {
    width: 1200px;
    height: 901px;
    overflow: hidden;
    background: var(--backdrop);
    font-family: "Quicksand", sans-serif;
  }
  .sheet {
    width: 1200px;
    height: 901px;
    display: flex;
    align-items: center;
    justify-content: center;
    gap: 40px;
  }
  .card {
    position: relative;
    width: 540px;
    height: 330px;
    background: var(--card);
    border-radius: 3px;
    box-shadow: 0 6px 18px rgba(0, 0, 0, 0.35);
    color: var(--text-blue);
  }

  /* Front: name side */
  .card-front {
    display: flex;
    align-items: center;
    justify-content: center;
  }
  .brand-name {
    font-size: 70px;
    font-weight: 600;
    letter-spacing: 4px;
    color: var(--brand-blue);
  }

  /* Back: contact side */
  .holder {
    position: absolute;
    top: 40px;
    left: 36px;
  }
  .holder-name {
    font-size: 19px;
    font-weight: 700;
    letter-spacing: 2.5px;
  }
  .holder-title {
    margin: 4px 0 0 150px;
    font-size: 11px;
    font-weight: 600;
    letter-spacing: 1.5px;
  }
  .contact-list {
    position: absolute;
    top: 96px;
    right: 30px;
    list-style: none;
    text-align: right;
    font-size: 11px;
    font-weight: 600;
    letter-spacing: 1.4px;
    line-height: 19px;
  }
  .address {
    position: absolute;
    left: 36px;
    bottom: 34px;
    font-size: 11px;
    font-weight: 700;
    letter-spacing: 1.6px;
  }
</style>
</head>
<body>
  <main class="sheet">
    <section class="card card-front" aria-label="Card front">
      <span class="brand-name">Vendora</span>
    </section>

    <section class="card card-back" aria-label="Card back">
      <div class="holder">
        <p class="holder-name">Gerald Huxton</p>
        <p class="holder-title">Director</p>
      </div>
      <ul class="contact-list">
        <li>Phone: +61 3 527 481 903</li>
        <li>Fax: +61 3 9254 3718</li>
        <li>Email: gerald.huxton@vendora-example.com.au</li>
        <li>LinkedIn: au.linkedin.com/in/geraldphuxton</li>
        <li>Twitter: @geraldphuxton</li>
        <li>Website: www.vendora-example.com.au</li>
      </ul>
      <p class="address">Level 7, 82 Fernhill Road, Melbourne, Australia, 3000</p>
    </section>
  </main>
</body>
</html>
```